Business Card Design Project

Recently had a new logo made up for my company and new business cards done as well. I have attached the logos for your viewing. Additional projects may be needed. Good luck!

Industry/Entity Type

Business

```html
<!DOCTYPE html>
<html lang="en">
<head>
<meta charset="utf-8">
<title>Harlow Crest Financial Group – Business Card</title>
<link rel="stylesheet" href="https://fonts.googleapis.com/css2?family=Jost:wght@400;500&family=Exo+2:wght@300&display=swap">
<style>
  :root {
    --backdrop: #958f7c;
    --card: #22222b;
    --gold: #cdb98a;
    --white: #ffffff;
    --blue: #1aa3e8;
    --globe-sea: #2f8fd6;
    --globe-land: #4caf50;
  }
  * { margin: 0; padding: 0; box-sizing: border-box; }
  html, body {
    width: 1200px; height: 1000px; overflow: hidden;
    background: var(--backdrop);
    font-family: "Jost", "Futura", sans-serif;
  }
  .card {
    position: absolute;
    background: var(--card);
    border-radius: 22px;
    overflow: hidden;
  }
  .card--front { left: 260px; top: 37px; width: 727px; height: 414px; }
  .card--back  { left: 260px; top: 502px; width: 730px; height: 416px; }

  .edge-tab { position: absolute; width: 16px; }
  .edge-tab--white { background: var(--white); top: 183px; height: 80px; }
  .edge-tab--gold  { background: var(--gold); top: 270px; height: 96px; }
  .edge-tab--left  { left: 0; }
  .edge-tab--right { right: 0; }

  .brand { position: absolute; color: var(--gold); font-weight: 500; }
  .brand__square { display: block; background: var(--gold); }
  .brand--front { left: 40px; top: 120px; width: 260px; }
  .brand--front .brand__square { width: 36px; height: 36px; margin-bottom: 18px; }
  .brand--front .brand__name { font-size: 44px; line-height: 1.05; letter-spacing: 0.5px; }
  .brand--front .brand__sub { font-size: 29px; line-height: 1.2; letter-spacing: 1px; }

  .person { position: absolute; left: 336px; top: 30px; }
  .person__name { color: var(--white); font-size: 24px; font-weight: 500; line-height: 1.3; }
  .person__role { color: var(--blue); font-size: 24px; font-weight: 500; line-height: 1.3; }

  .contact { position: absolute; left: 331px; top: 142px; color: var(--gold); font-size: 19px; font-weight: 500; }
  .contact__line { line-height: 1.2; margin-bottom: 8px; white-space: nowrap; }
  .contact__label { color: var(--blue); }
  .contact__address { line-height: 1.1; }

  .website { position: absolute; left: 326px; top: 364px; display: flex; align-items: center; gap: 8px;
    color: var(--gold); font-size: 21px; font-weight: 500; }
  .website__icon { width: 26px; height: 26px; }

  .brand--back { left: 0; right: 0; top: 112px; text-align: center; }
  .brand--back .brand__square { width: 40px; height: 40px; margin: 0 auto 22px; }
  .brand--back .brand__name { font-size: 36px; line-height: 1.1; }

  .tagline { position: absolute; left: 0; right: 0; top: 282px; text-align: center;
    font-family: "Exo 2", sans-serif; font-weight: 300; font-size: 29px; letter-spacing: 0.5px; color: var(--gold); }
  .tagline__joiner { color: var(--white); }
</style>
</head>
<body>
  <section class="card card--front">
    <span class="edge-tab edge-tab--white edge-tab--left"></span>
    <span class="edge-tab edge-tab--gold edge-tab--left"></span>
    <span class="edge-tab edge-tab--white edge-tab--right"></span>
    <span class="edge-tab edge-tab--gold edge-tab--right"></span>

    <div class="brand brand--front">
      <span class="brand__square"></span>
      <div class="brand__name">Harlow Crest</div>
      <div class="brand__sub">Financial Group</div>
    </div>

    <div class="person">
      <div class="person__name">Daniel R. Whitcombe</div>
      <div class="person__role">Director</div>
    </div>

    <div class="contact">
      <p class="contact__line"><span class="contact__label">E:</span> dwhitcombe@harlowcrest.com</p>
      <p class="contact__line"><span class="contact__label">P:</span> 555-210-4837 <span class="contact__label">F:</span> 555-210-4852</p>
      <p class="contact__line contact__address">4120 Meadowbrook Parkway, Suite 310E<br>Glenwood, New York 11590</p>
    </div>

    <div class="website">
      <svg class="website__icon" viewBox="0 0 26 26" aria-hidden="true">
        <circle cx="13" cy="13" r="12" fill="var(--globe-sea)"/>
        <path d="M6 8 q4 -3 7 0 q1 3 -2 5 q-3 1 -2 5 q-4 -2 -4 -6 z" fill="var(--globe-land)"/>
        <path d="M16 14 q4 -1 5 2 q-1 4 -5 5 q-2 -3 0 -7 z" fill="var(--globe-land)"/>
      </svg>
      <span>www.harlowcrest.com</span>
    </div>
  </section>

  <section class="card card--back">
    <div class="brand brand--back">
      <span class="brand__square"></span>
      <div class="brand__name">Harlow Crest Financial Group</div>
    </div>
    <p class="tagline">Estate Planning <span class="tagline__joiner">and</span> Insurance Specialist</p>
  </section>
</body>
</html>
```